WEBSITE DESIGN - www.brondellix.com

We need a professional and modern looking website for our business. The current website was only made tentatively and can be viewed (we expect a website MUCH better than this). It needs to be simple and non-cluttered yet look modern and sophisticated. It needs to be very easy to navigate as our tarket market is people over the age of 45. Our logo is attached below and this should be incorporated plus the colours/theme should match this. We don't mind purchasing images online if your design includes these and we like it.

Any other specific questions please enquire as we want to hear them.

Target Market(s)

over 45 age english speaking westerners

Industry/Entity Type

Business

Number of Pages Required

1 page

Requirements
Must have
• -our logo (attached).
• -page tabs as those described (tabs.. but not necessarily each of these pages completed as well although this would be nice).
• -social media logos
• Pages should include: homepage, services, pricing, about us, contact us. There should also be a payments page designed which would link with the other pages but there would be no tab for this.

```html
<!DOCTYPE html>
<html lang="en">
<head>
<meta charset="utf-8">
<title>Brondellix – Computer Solutions</title>
<link href="https://fonts.googleapis.com/css2?family=Open+Sans:wght@400;600;700;800&display=swap" rel="stylesheet">
<style>
:root{
  --orange:#f7a81b;
  --orange-dark:#e59400;
  --ink:#1d1d1d;
  --text:#444;
  --muted:#777;
  --grey:#8b8b8b;
  --light:#f2f2f2;
  --dark:#141414;
  --white:#fff;
}
*{box-sizing:border-box;margin:0;padding:0}
html,body{width:1200px;height:4569px;overflow:hidden}
body{font-family:"Open Sans",Arial,sans-serif;color:var(--text);background:var(--white)}
.section-title{font-size:30px;font-weight:700;color:var(--ink);text-align:center;letter-spacing:.5px}
.on-dark .section-title{color:var(--white)}

/* header + hero */
.hero{position:relative;height:563px;background:linear-gradient(135deg,#4a5466 0%,#8d98a8 45%,#dfe3e8 75%,#9aa3ae 100%)}
.logo{position:absolute;left:0;top:0;width:350px;height:146px;background:var(--white);display:flex;align-items:center;justify-content:center;gap:14px}
.logo-mark{width:40px;height:40px;border-radius:50%;background:var(--ink)}
.logo-name{font-size:42px;font-weight:600;color:var(--ink)}
.nav{position:absolute;right:0;top:0;height:55px;width:750px;background:rgba(0,0,0,.85);display:flex;justify-content:flex-end}
.nav a{display:flex;align-items:center;padding:0 30px;color:var(--white);font-size:16px;font-weight:600;text-decoration:none;text-transform:uppercase;white-space:nowrap}
.nav a.active{background:var(--orange)}
.hero-copy{position:absolute;left:30px;top:235px;color:var(--white)}
.hero-copy h1{font-size:33px;font-weight:800;letter-spacing:.3px}
.hero-copy p{font-size:26px;font-weight:600;line-height:36px;margin-top:12px;width:560px}
.hero-btns{display:flex;gap:18px;margin-top:34px}
.btn{display:inline-block;padding:12px 26px;border-radius:30px;font-size:19px;font-weight:600;text-decoration:none}
.btn-solid{background:var(--orange);color:var(--ink)}
.btn-ghost{border:2px solid var(--white);color:var(--white)}

/* welcome */
.welcome{height:610px;padding-top:30px;text-align:center}
.welcome .tag{color:var(--orange-dark);font-size:18px;font-weight:700;margin-top:46px}
.welcome .intro{width:1100px;margin:14px auto 0;font-size:18px;line-height:28px;text-align:left}
.phones{display:flex;justify-content:center;gap:18px;margin-top:40px}
.pill{display:inline-block;height:44px;line-height:26px;background:var(--orange);color:var(--ink);font-size:19px;border-radius:28px;padding:9px 24px;min-width:220px}
.pill-wide{min-width:305px}
.devices{display:flex;justify-content:space-between;width:1160px;margin:30px auto 0}
.device{width:165px;text-align:center}
.device .disc{width:124px;height:124px;border-radius:50%;background:var(--grey);margin:0 auto;display:flex;align-items:center;justify-content:center}
.device.active .disc{background:var(--orange)}
.device .num{font-size:18px;font-weight:600;color:var(--ink);margin-top:12px}
.device.active .num{color:var(--orange)}
.device .lbl{font-size:17px;color:var(--text);margin-top:4px}

/* why */
.why{position:relative;height:709px;background:var(--orange);overflow:hidden}
.why .section-title{padding-top:40px}
.why .sub{text-align:center;font-size:16px;color:var(--ink);margin-top:14px}
.why-list{position:absolute;left:24px;top:162px;width:580px;display:flex;flex-direction:column;gap:14px}
.why-item{display:flex;background:var(--white);border-radius:10px;height:106px;align-items:center;padding:0 14px;gap:18px}
.why-item .ico{flex:none;width:74px;height:74px;border-radius:50%;background:var(--orange);display:flex;align-items:center;justify-content:center}
.why-item.first .ico{border-radius:8px;background:var(--ink)}
.why-item h3{font-size:16px;font-weight:700;color:var(--orange-dark);text-transform:uppercase}
.why-item.first h3{color:var(--ink)}
.why-item p{font-size:15px;line-height:21px;color:var(--ink);margin-top:3px}
.why-photo{position:absolute;left:610px;top:125px;width:590px;height:584px;background:radial-gradient(ellipse at 50% 45%,#f4dcc6 0%,#e8b58f 30%,#f2f2f2 55%,var(--orange) 80%)}

/* stats */
.stats{height:296px;display:flex;justify-content:space-around;padding:22px 10px 0}
.stat{width:180px;text-align:center}
.ring{position:relative;width:170px;height:170px;margin:0 auto}
.ring span{position:absolute;inset:0;display:flex;align-items:center;justify-content:center;font-size:30px;font-weight:700;color:var(--ink)}
.stat .lbl{font-size:17px;color:var(--ink);text-transform:uppercase;margin-top:14px;line-height:22px}

/* testimonials */
.reviews{height:305px;background:var(--dark);padding-top:44px}
.review-row{display:flex;justify-content:center;gap:30px;margin-top:30px}
.review{display:flex;align-items:center}
.avatar{width:124px;height:124px;border-radius:50%;background:linear-gradient(160deg,#cfd4da,#6e7781);border:4px solid var(--white);position:relative;z-index:1}
.review .bubble{background:var(--white);width:420px;height:130px;margin-left:-10px;padding:14px 20px 14px 30px;font-size:14px;line-height:20px;color:var(--muted)}
.review .bubble b{display:block;color:var(--orange-dark);margin-top:8px;font-weight:700}
.dots{display:flex;justify-content:center;gap:8px;margin-top:18px}
.dots i{width:12px;height:12px;border-radius:50%;background:#555}
.dots i.on{background:var(--orange)}

/* services */
.services{height:441px;padding-top:96px}
.svc-grid{display:grid;grid-template-columns:565px 565px;gap:45px 24px;justify-content:center;margin-top:40px}
.svc{position:relative;height:107px;border-radius:12px;padding:14px 110px 0 18px}
.svc.outline{border:4px solid var(--orange);background:var(--white)}
.svc.filled{background:var(--orange)}
.svc h3{font-size:16px;font-weight:700;text-transform:uppercase;color:var(--orange-dark)}
.svc.filled h3{color:var(--white)}
.svc p{font-size:16px;line-height:22px;color:var(--ink);margin-top:4px}
.svc.filled p{color:var(--white)}
.svc .tab{position:absolute;right:0;top:0;bottom:0;width:96px;display:flex;align-items:center;justify-content:center}
.svc .tab .c{width:76px;height:76px;border-radius:50%;display:flex;align-items:center;justify-content:center}
.svc.outline .tab .c{background:var(--white);border:3px solid var(--orange)}
.svc.filled .tab .c{background:var(--orange-dark);border:3px solid var(--white)}

/* plans */
.plans{height:701px;background:linear-gradient(#1b1b1b,#0c0c0c);padding-top:62px}
.plan-row{display:flex;justify-content:center;align-items:flex-start;gap:20px;margin-top:30px}
.plan{width:355px;background:var(--white);text-align:center;padding:28px 22px 24px;margin-top:62px;height:472px}
.plan.featured{margin-top:28px;height:548px}
.plan .badge{display:inline-block;background:var(--orange);color:var(--white);padding:8px 22px;font-weight:700;font-size:16px;text-transform:uppercase;line-height:20px}
.plan .badge small{display:block;font-size:11px;font-weight:600;text-transform:none}
.plan .price{font-size:20px;font-weight:700;color:#555;margin:22px 0 14px}
.plan .note{font-size:16px;color:#444;line-height:22px;margin-bottom:10px}
.plan ul{list-style:none;border-top:1px solid #ddd}
.plan li{font-size:15px;color:#444;padding:13px 0;border-bottom:1px solid #ddd}
.plan .agree{display:flex;align-items:center;gap:8px;font-size:15px;color:var(--ink);margin:24px 0 16px}
.plan .agree i{width:16px;height:16px;border:1px solid #666}
.plan .go{display:inline-block;border:1px solid #888;color:#555;padding:8px 26px;font-size:15px;text-transform:uppercase}
.plan.featured .go{background:var(--orange);border-color:var(--orange);color:var(--white);font-weight:700}

/* payments */
.payments{height:243px;display:flex;align-items:center;justify-content:center;gap:22px}
.arrow{width:36px;height:36px;border-radius:50%;border:1px solid #ccc;display:flex;align-items:center;justify-content:center}
.card-box{width:148px;height:108px;border:1px solid #ddd;display:flex;align-items:center;justify-content:center;background:var(--white)}
.card-box span{font-size:17px;font-weight:700;color:var(--ink)}
.card-box .shape{width:80px;height:80px;border-radius:50%;background:#d7d7d7}

/* keep in touch */
.touch{height:473px;background:linear-gradient(#202020,#111);color:var(--white);padding-top:66px}
.contact-info{display:flex;justify-content:space-between;width:1140px;margin:40px auto 0}
.ci{display:flex;gap:16px;width:360px;font-size:15px;line-height:21px}
.ci .c{flex:none;width:58px;height:58px;border-radius:50%;border:3px solid var(--orange);display:flex;align-items:center;justify-content:center}
.form{width:1160px;margin:34px auto 0}
.form .row{display:flex;gap:25px}
.field{flex:1;height:48px;background:#1c1c1c;border:1px solid #333;color:#bbb;font-size:15px;padding:13px 14px}
.form .msg{display:flex;gap:25px;margin-top:26px}
.field.area{height:108px}
.send{width:130px;height:108px;background:var(--orange);color:var(--white);font-size:26px;font-weight:700;display:flex;align-items:center;justify-content:center}

/* footer */
.footer{height:228px;text-align:center;padding-top:50px;font-size:14px;color:var(--text)}
.footer .copy{margin-top:44px}
.footer .copy b{color:var(--orange-dark);font-weight:600}
.socials{display:flex;justify-content:center;gap:10px;margin-top:24px}
.socials i{width:30px;height:30px;border-radius:50%;background:var(--orange)}
.socials i.grey{background:#bbb}
</style>
</head>
<body>

<header class="hero">
  <div class="hero-bg" role="img" aria-label="Photo of desktop monitors, laptops and tablets showing website layouts" style="position:absolute;inset:0"></div>
  <div class="logo"><span class="logo-mark"></span><span class="logo-name">Brondellix</span></div>
  <nav class="nav">
    <a class="active" href="#">Home</a><a href="#">Intro</a><a href="#">About Us</a><a href="#">Services</a><a href="#">Pricing</a><a href="#">Contact</a>
  </nav>
  <div class="hero-copy">
    <h1>WE PROVIDE BEST WEB DESIGN SERVICE</h1>
    <p>We understand that every business owner has his own way of showcasing products</p>
    <div class="hero-btns"><a class="btn btn-solid" href="#">Learn More</a><a class="btn btn-ghost" href="#">See Work</a></div>
  </div>
</header>

<section class="welcome">
  <h2 class="section-title">WELCOME TO BRONDELLIX</h2>
  <div class="tag">OUR CUSTOMER OUR PRIORITY LETS SAY HI.</div>
  <p class="intro">Brondellix was established to provide consumers with access to the sophisticated, enterprise-level IT services, support and the benefits and cost savings,available to larger organisations.We provide proactive monitoring and management of &nbsp;customers entire IT needs. Brondellix is a growing organisation dedicated to making your PC tech support easy and</p>
  <div class="phones">
    <span class="pill">USA +1 555 014 2290</span><span class="pill">UK +44 20 7946 0318</span><span class="pill">AUS +61 2 5550 1942</span><span class="pill pill-wide">Contact Us</span>
  </div>
  <div class="devices">
    <div class="device active"><div class="disc"><svg width="64" height="48" viewBox="0 0 64 48"><rect x="10" y="4" width="44" height="30" rx="2" fill="none" stroke="#fff" stroke-width="4"/><rect x="2" y="38" width="60" height="6" rx="2" fill="#fff"/></svg></div><div class="num">986</div><div class="lbl">Laptop</div></div>
    <div class="device"><div class="disc"><svg width="64" height="48" viewBox="0 0 64 48"><rect x="6" y="22" width="52" height="18" rx="3" fill="none" stroke="#fff" stroke-width="4"/><path d="M16 22V6M48 22V6" stroke="#fff" stroke-width="4"/><circle cx="18" cy="31" r="3" fill="#fff"/><circle cx="28" cy="31" r="3" fill="#fff"/></svg></div><div class="num">256</div><div class="lbl">Routers</div></div>
    <div class="device"><div class="disc"><svg width="40" height="60" viewBox="0 0 40 60"><rect x="4" y="2" width="32" height="56" rx="5" fill="none" stroke="#fff" stroke-width="4"/><circle cx="20" cy="49" r="3" fill="#fff"/></svg></div><div class="num">867</div><div class="lbl">Smart Phones</div></div>
    <div class="device"><div class="disc"><svg width="64" height="56" viewBox="0 0 64 56"><rect x="4" y="4" width="56" height="36" rx="2" fill="none" stroke="#fff" stroke-width="4"/><path d="M26 40v8M38 40v8M18 50h28" stroke="#fff" stroke-width="4"/></svg></div><div class="num">1904</div><div class="lbl">Desktops</div></div>
    <div class="device"><div class="disc"><svg width="48" height="60" viewBox="0 0 48 60"><rect x="4" y="2" width="40" height="56" rx="5" fill="none" stroke="#fff" stroke-width="4"/><circle cx="24" cy="50" r="3" fill="#fff"/></svg></div><div class="num">511</div><div class="lbl">Tablets</div></div>
    <div class="device"><div class="disc"><svg width="64" height="56" viewBox="0 0 64 56"><rect x="4" y="4" width="56" height="36" rx="2" fill="none" stroke="#fff" stroke-width="4"/><path d="M22 22h20M34 14l8 8-8 8M20 50h24" stroke="#fff" stroke-width="4" fill="none"/></svg></div><div class="num">2456</div><div class="lbl">Software Installation</div></div>
  </div>
</section>

<section class="why">
  <h2 class="section-title">WHY WE ARE THE BEST</h2>
  <p class="sub">The one stop comprehensive diagnostic &amp; repair station for your computer and connected devices.We'll fix anything!</p>
  <div class="why-list">
    <div class="why-item first"><div class="ico"><svg width="40" height="36" viewBox="0 0 40 36"><rect x="2" y="2" width="36" height="24" fill="none" stroke="#fff" stroke-width="3"/><path d="M12 34h16M20 26v8" stroke="#fff" stroke-width="3"/></svg></div><div><h3>Diagnosis &amp; Repair</h3><p>The one stop comprehensive diagnostic &amp; repair station for your computer and connected devices. We'll fix anything!</p></div></div>
    <div class="why-item"><div class="ico"><svg width="40" height="40" viewBox="0 0 40 40"><circle cx="20" cy="20" r="8" fill="none" stroke="#fff" stroke-width="4"/><path d="M20 2v8M20 30v8M2 20h8M30 20h8" stroke="#fff" stroke-width="4"/></svg></div><div><h3>Setup &amp; Install</h3><p>Confused and frustrated with device setup &amp; installation? Leave it</p></div></div>
    <div class="why-item"><div class="ico"><svg width="40" height="36" viewBox="0 0 40 36"><rect x="2" y="2" width="36" height="26" fill="none" stroke="#fff" stroke-width="3"/><path d="M8 22l8-8 6 5 10-10" stroke="#fff" stroke-width="3" fill="none"/></svg></div><div><h3>Optimization</h3><p>You won't believe it's the same old computer. Your system will work like it did on the day you bought it</p></div></div>
    <div class="why-item"><div class="ico"><svg width="40" height="40" viewBox="0 0 40 40"><path d="M6 24v-4a14 14 0 0 1 28 0v4" fill="none" stroke="#fff" stroke-width="3"/><rect x="4" y="22" width="7" height="12" rx="2" fill="#fff"/><rect x="29" y="22" width="7" height="12" rx="2" fill="#fff"/></svg></div><div><h3>Support</h3><p>We develop the website, we analyse, strategize and assess our client's specific need,requirement,preference</p></div></div>
  </div>
  <div class="why-photo" role="img" aria-label="Photo of a smiling woman in a white shirt with hands behind her head"></div>
</section>

<section class="stats">
  <div class="stat"><div class="ring"><svg width="170" height="170" viewBox="0 0 170 170"><circle cx="85" cy="85" r="72" fill="none" stroke="#f7a81b" stroke-width="22"/><circle cx="85" cy="85" r="72" fill="none" stroke="#1d1d1d" stroke-width="10" stroke-dasharray="430 453" transform="rotate(-90 85 85)"/></svg><span>95%</span></div><div class="lbl">Awesomeness</div></div>
  <div class="stat"><div class="ring"><svg width="170" height="170" viewBox="0 0 170 170"><circle cx="85" cy="85" r="72" fill="none" stroke="#f7a81b" stroke-width="22"/><circle cx="85" cy="85" r="72" fill="none" stroke="#1d1d1d" stroke-width="10" stroke-dasharray="444 453" transform="rotate(-90 85 85)"/></svg><span>98%</span></div><div class="lbl">Flexibility</div></div>
  <div class="stat"><div class="ring"><svg width="170" height="170" viewBox="0 0 170 170"><circle cx="85" cy="85" r="72" fill="none" stroke="#f7a81b" stroke-width="22"/><circle cx="85" cy="85" r="72" fill="none" stroke="#1d1d1d" stroke-width="10" stroke-dasharray="421 453" transform="rotate(-90 85 85)"/></svg><span>93%</span></div><div class="lbl">Virus<br>Removal</div></div>
  <div class="stat"><div class="ring"><svg width="170" height="170" viewBox="0 0 170 170"><circle cx="85" cy="85" r="72" fill="none" stroke="#f7a81b" stroke-width="22"/><circle cx="85" cy="85" r="72" fill="none" stroke="#1d1d1d" stroke-width="10"/></svg><span>100%</span></div><div class="lbl">Support</div></div>
  <div class="stat"><div class="ring"><svg width="170" height="170" viewBox="0 0 170 170"><circle cx="85" cy="85" r="72" fill="none" stroke="#f7a81b" stroke-width="22"/><circle cx="85" cy="85" r="72" fill="none" stroke="#1d1d1d" stroke-width="10" stroke-dasharray="439 453" transform="rotate(-90 85 85)"/></svg><span>97%</span></div><div class="lbl">Software<br>Installation</div></div>
  <div class="stat"><div class="ring"><svg width="170" height="170" viewBox="0 0 170 170"><circle cx="85" cy="85" r="72" fill="none" stroke="#f7a81b" stroke-width="22"/><circle cx="85" cy="85" r="72" fill="none" stroke="#1d1d1d" stroke-width="10" stroke-dasharray="444 453" transform="rotate(-90 85 85)"/></svg><span>98%</span></div><div class="lbl">System<br>Setup</div></div>
</section>

<section class="reviews on-dark">
  <h2 class="section-title">WHAT PEOPLE SAY ABOUT US</h2>
  <div class="review-row">
    <div class="review"><div class="avatar" role="img" aria-label="Customer portrait photo"></div><div class="bubble">Thank for such a Support, Quality Support. I'm extremely impressed. It has been one of the best experiences.So pleased with Brondellix,You r'd best.<b>Mara Linwood</b></div></div>
    <div class="review"><div class="avatar" role="img" aria-label="Customer portrait photo"></div><div class="bubble">Thanks Brondellix,That was huge help and exactly what i was looking for. I appreciate the help you probably saved me 5 hours of frustration right.<b>Dana Holloway</b></div></div>
  </div>
  <div class="dots"><i class="on"></i><i></i><i></i></div>
</section>

<section class="services">
  <h2 class="section-title">OUR SERVICES</h2>
  <div class="svc-grid">
    <div class="svc outline"><h3>Tech Support</h3><p>We make technology easier for you with instant support.</p><div class="tab"><div class="c"><svg width="40" height="34" viewBox="0 0 40 34"><rect x="2" y="2" width="36" height="22" fill="none" stroke="#f7a81b" stroke-width="3"/><path d="M12 32h16" stroke="#f7a81b" stroke-width="3"/></svg></div></div></div>
    <div class="svc filled"><h3>Downloads</h3><p>The best apps to optimize &amp; secure your digital devices.</p><div class="tab"><div class="c"><svg width="40" height="34" viewBox="0 0 40 34"><path d="M10 26a9 9 0 0 1 2-18 11 11 0 0 1 20 4 7 7 0 0 1-2 14z" fill="#fff"/><path d="M21 12v12M16 19l5 5 5-5" stroke="#e59400" stroke-width="3" fill="none"/></svg></div></div></div>
    <div class="svc filled"><h3>Web Design</h3><p>We understand that every business owner has his own way of showcasing products</p><div class="tab"><div class="c"><svg width="40" height="34" viewBox="0 0 40 34"><rect x="2" y="2" width="36" height="22" fill="none" stroke="#fff" stroke-width="3"/><path d="M12 32h16M14 18l12-10" stroke="#fff" stroke-width="3"/></svg></div></div></div>
    <div class="svc filled"><h3>Understand the Urgency</h3><p>We believe in careful planning for you.</p><div class="tab"><div class="c"><svg width="40" height="34" viewBox="0 0 40 34"><rect x="4" y="4" width="32" height="26" fill="none" stroke="#fff" stroke-width="3"/><path d="M4 12h32M12 20h16" stroke="#fff" stroke-width="3"/></svg></div></div></div>
  </div>
</section>

<section class="plans on-dark">
  <h2 class="section-title">OUR PLANS</h2>
  <div class="plan-row">
    <div class="plan"><span class="badge">Quick Fix<small>1 Month</small></span><div class="price">NZD 95 &nbsp;USD 60* &nbsp;GBP 40*</div><ul><li>1 Month Tech Support</li><li>For 1 Computer</li><li>24X7 Availability</li></ul><div class="agree"><i></i>I agree to the Terms and Conditions</div><span class="go">Get Start Now</span></div>
    <div class="plan featured"><span class="badge">Advance<small>1 Year</small></span><div class="price">NZD 250 &nbsp;USD 160* &nbsp;GBP 105*</div><p class="note">*The price advertised might not be the price charged to the credit card account due to exchange rate fluctuations.</p><ul><li>1 Month Tech Support</li><li>Upto 3 Computers &amp; Printers</li><li>Connected Devices with Router</li></ul><div class="agree"><i></i>I agree to the Terms and Conditions</div><span class="go">Get Start Now</span></div>
    <div class="plan"><span class="badge">Starter<small>6 Month</small></span><div class="price">NZD 140 &nbsp;USD 90* &nbsp;GBP 60*</div><ul><li>6 Month Tech Support</li><li>6 Month support for the same issue</li><li>24X7 Availability</li></ul><div class="agree"><i></i>I agree to the Terms and Conditions</div><span class="go">Get Start Now</span></div>
  </div>
</section>

<section class="payments">
  <span class="arrow"><svg width="12" height="14" viewBox="0 0 12 14"><path d="M9 2L3 7l6 5" stroke="#333" stroke-width="2" fill="none"/></svg></span>
  <div class="card-box"><span>Paylon</span></div>
  <div class="card-box"><span>Cardora</span></div>
  <div class="card-box"><span class="shape" aria-label="Secure shopping badge"></span></div>
  <div class="card-box"><span>Trevio</span></div>
  <div class="card-box"><span>Paylon Flex</span></div>
  <div class="card-box"><span>Orvanta</span></div>
  <span class="arrow"><svg width="12" height="14" viewBox="0 0 12 14"><path d="M3 2l6 5-6 5" stroke="#333" stroke-width="2" fill="none"/></svg></span>
</section>

<section class="touch on-dark">
  <h2 class="section-title">KEEP IN TOUCH WITH US</h2>
  <div class="contact-info">
    <div class="ci"><span class="c"><svg width="22" height="28" viewBox="0 0 22 28"><path d="M11 26S2 16 2 10a9 9 0 0 1 18 0c0 6-9 16-9 16z" fill="none" stroke="#f7a81b" stroke-width="3"/><circle cx="11" cy="10" r="3" fill="#f7a81b"/></svg></span><div>Marlow Court Tower 2<br>4B/118 Kestrel Street<br>Harbourside Central 1042<br>New Zealand</div></div>
    <div class="ci"><span class="c"><svg width="26" height="26" viewBox="0 0 26 26"><path d="M6 2l5 6-3 3c2 4 5 7 9 9l3-3 6 5-3 4C12 25 1 14 2 5z" fill="#f7a81b"/></svg></span><div>USA: +1 555 014 2290<br>UK: +44 20 7946 0318<br>Australia: +61 2 5550 1942</div></div>
    <div class="ci"><span class="c"><svg width="28" height="22" viewBox="0 0 28 22"><rect x="2" y="2" width="24" height="18" fill="none" stroke="#f7a81b" stroke-width="3"/><path d="M2 2l12 10L26 2" stroke="#f7a81b" stroke-width="3" fill="none"/></svg></span><div>For Query - info@brondellix.com<br>For Billing - bills@brondellix.com<br>For Support - support@brondellix.com</div></div>
  </div>
  <div class="form">
    <div class="row"><div class="field">Your Name</div><div class="field">Your E-mail</div><div class="field">Your Phone</div></div>
    <div class="msg"><div class="field area">Your Message</div><div class="send">SEND</div></div>
  </div>
</section>

<footer class="footer">
  <p>We do not take payments through Corvane Transfer. We are not associated with Veltrix, Norvane, Kestro, Quillon, or any other Brands.<br>We are Third Party Tech Support Company.</p>
  <p class="copy">Copyright © 2016 <b>Brondellix</b>. All rights reserved.</p>
  <div class="socials" aria-label="Social media links"><i></i><i class="grey"></i><i class="grey"></i><i class="grey"></i></div>
</footer>

</body>
</html>
```